Renewable Energy company needs a new website

We are renewable energy company that has been operating for 3 years now and require a new website design. We are looking to upgrade our website to be comparable to our competitors. We are not a brick and mortar business so our website does need to be very appealing and convey a sense of authenticity and trust to the consumer. It will also heavily display our current system special and offering etc. The final design needs to be visually appealing in a marketing sense however also needs to convey a high sense of professionalism.

Target Market(s)

Consumers of solar systems for installation on their home or business.

Coding

Coded - Design and coding required

Number of Pages Required

3 page

Font styles to use
Sans Serif

Colors

Designer to choose colors to be used in the design.

Requirements
Must have
• A home page, a page for residential solar systems including the packages we are currently offering and a commercial page for larger installations of solar systems.
• www.torvapower.com.au
Nice to have
• As a template we do like this https://www.bluneklight.com.au/qld/ in terms of design elements and layout of the page.

```html
<!DOCTYPE html>
<html lang="en">
<head>
<meta charset="utf-8">
<title>Torva Power — Solar for Home and Business</title>
<link href="https://fonts.googleapis.com/css2?family=Poppins:ital,wght@0,400;0,500;0,600;0,700;1,400&display=swap" rel="stylesheet">
<style>
:root{
  --red:#c8222b;
  --red-soft:#d23a42;
  --ink:#2b2f38;
  --muted:#6d717a;
  --navy:#2d3340;
  --yellow:#f5cf0c;
  --line:#e4e6ea;
  --grey-a:#c9ccd2;
  --grey-b:#eef0f3;
  --white:#fff;
}
*{box-sizing:border-box;margin:0;padding:0}
html,body{width:1200px;height:4996px;overflow:hidden;background:var(--white)}
body{font-family:'Poppins',sans-serif;color:var(--ink);position:relative}
.abs{position:absolute}
a{color:inherit;text-decoration:none}
.brand{display:flex;align-items:center;gap:10px}
.brand-mark{width:34px;height:34px;background:var(--red)}
.brand-name{font-weight:700;font-size:24px;color:var(--red);letter-spacing:.5px;text-transform:uppercase}
.brand-tag{font-size:8px;color:var(--muted);letter-spacing:.5px;margin-top:2px}

/* header */
.site-header{top:0;left:0;width:1200px;height:100px}
.nav{top:40px;left:448px;display:flex;gap:45px;font-size:13px;font-weight:500}
.btn-call{top:24px;left:788px;width:198px;height:48px;background:var(--navy);color:#fff;font-size:12px;font-weight:600;display:flex;align-items:center;justify-content:center;gap:8px}
.btn-quote{top:24px;left:1000px;width:110px;height:48px;background:var(--red);color:#fff;font-size:12px;font-weight:600;display:flex;align-items:center;justify-content:center}

/* hero */
.hero{top:100px;left:0;width:1200px;height:580px}
.hero-title{top:210px;left:88px;font-size:25px;font-weight:600;letter-spacing:.5px}
.hero-sub{top:247px;left:88px;font-size:19px;color:var(--ink)}
.old-price{top:310px;left:90px;font-size:21px;color:var(--muted);text-decoration:line-through}
.new-price{top:286px;left:184px;font-size:58px;font-weight:700;color:var(--red)}
.btn-dark{background:var(--navy);color:#fff;font-size:11px;font-weight:600;display:flex;align-items:center;justify-content:center}
.save{top:112px;left:488px;display:flex;gap:6px}
.save span{width:54px;height:54px;border-radius:50%;background:#1e8fd6;color:#fff;font-weight:700;font-size:26px;display:flex;align-items:center;justify-content:center}
.power-title{top:180px;left:735px;font-size:30px;font-weight:600;display:flex;align-items:baseline;gap:10px}
.power-title b{color:var(--yellow);font-size:58px;font-weight:700;line-height:1}
.feat{font-size:13px;display:flex;align-items:center;gap:8px}
.feat i{width:13px;height:13px;border:2px solid var(--red);border-radius:50%;display:inline-block}

/* cards */
.svc{top:752px;width:242px;height:346px;background:#fff;box-shadow:0 6px 22px rgba(0,0,0,.09);padding:16px}
.svc .ph{width:210px;height:150px}
.svc h3{font-size:12px;font-weight:700;margin-top:22px;line-height:1.35;text-transform:uppercase}
.svc p{font-size:11px;color:var(--muted);margin-top:12px;line-height:1.5}
.more{display:flex;align-items:center;gap:8px;font-size:11px;font-weight:600;color:var(--red);margin-top:14px}
.more i{width:24px;height:24px;border-radius:50%;background:var(--red);display:inline-flex;align-items:center;justify-content:center}

.headline{top:1180px;left:0;width:1200px;text-align:center;font-size:27px;font-weight:600}
.headline b{color:var(--red);font-size:38px;font-weight:700}
.lede{top:1238px;left:200px;width:800px;text-align:center;font-size:12px;color:var(--muted);line-height:1.7}

/* quote form */
.quote-box{top:1346px;left:88px;width:737px;height:656px;background:var(--red);overflow:hidden}
.quote-box h2{position:absolute;top:68px;left:56px;color:#fff;font-size:27px;font-weight:600}
.quote-box .q-sub{position:absolute;top:108px;left:56px;color:#fff;font-size:12px}
.field{position:absolute;background:var(--red-soft);color:#fff;font-size:13px;padding:0 18px;display:flex;align-items:center}
.field.tall{align-items:flex-start;padding-top:16px}
.btn-white{position:absolute;left:56px;top:496px;width:460px;height:44px;background:#fff;color:var(--ink);font-size:13px;font-weight:600;display:flex;align-items:center;justify-content:center}

.sec-title{left:0;width:1200px;text-align:center;font-size:25px;font-weight:600;text-transform:uppercase}
.prod{top:2130px;width:236px}
.prod .box{height:310px;background:linear-gradient(#fff,#f4f5f7);box-shadow:0 6px 22px rgba(0,0,0,.08);display:flex;align-items:center;justify-content:center}
.prod h4{text-align:center;font-size:16px;font-weight:600;margin-top:30px}
.prod .price{text-align:center;font-size:26px;font-weight:700;color:var(--yellow);margin-top:2px}
.prod .btn-red{margin:10px auto 0;width:110px;height:38px;background:var(--red);color:#fff;font-size:10px;font-weight:600;display:flex;align-items:center;justify-content:center}
.rule{left:88px;width:1024px;height:1px;background:var(--line)}

.grow-card{top:3060px;width:460px;height:172px;background:#fff;box-shadow:0 6px 22px rgba(0,0,0,.1);padding:26px 26px}
.grow-card h3{font-size:14px;font-weight:600;line-height:1.35;text-transform:uppercase}
.grow-card p{font-size:11.5px;color:var(--muted);margin-top:12px;line-height:1.6}

.why{top:3366px;width:190px;text-align:center}
.why .icon{width:110px;height:110px;border-radius:50%;background:var(--red);margin:0 auto;display:flex;align-items:center;justify-content:center}
.why .icon.dark{background:var(--navy)}
.why p{font-size:11px;font-weight:600;margin-top:22px;line-height:1.4;text-transform:uppercase}

.feature-text{top:3658px;left:686px;width:426px}
.feature-text h2{font-size:26px;font-weight:600;line-height:1.2;text-transform:uppercase}
.feature-text p{font-size:15px;color:var(--muted);margin-top:20px;line-height:1.65}

.avatar{border-radius:50%;top:0}
.testi{top:4226px;left:300px;width:600px;text-align:center}
.stars{color:#f5b400;font-size:20px;letter-spacing:2px}
.testi q{display:block;font-style:italic;font-size:15px;color:var(--muted);line-height:1.75;margin-top:4px;quotes:none}
.testi .name{color:var(--red);font-weight:600;font-size:13px;margin-top:30px}
.testi .role{font-size:12px;color:var(--muted)}
.qmark{font-size:100px;color:#e2e4e8;font-weight:700;line-height:1}

/* footer */
.footer{top:4582px;left:0;width:1200px;height:414px;background:var(--navy);color:#fff}
.f-col h5{font-size:14px;font-weight:600;margin-bottom:14px;text-transform:uppercase}
.f-col li{list-style:none;font-size:12px;line-height:25px;color:#e8eaee}
.contact-item{display:flex;gap:12px;margin-bottom:14px}
.contact-item b{font-size:13px;font-weight:600;display:block}
.contact-item span{font-size:11.5px;color:#e8eaee}
.copy{position:absolute;left:0;top:386px;width:1200px;text-align:center;font-size:12px}
.to-top{position:absolute;left:1131px;top:352px;width:38px;height:38px;border-radius:50%;background:var(--red);display:flex;align-items:center;justify-content:center}
</style>
</head>
<body>

<header class="site-header abs">
  <div class="brand abs" style="top:22px;left:88px">
    <span class="brand-mark"></span>
    <div><div class="brand-name">Torva Power</div><div class="brand-tag">ENGINEERING AND ECONOMIC SOLUTIONS</div></div>
  </div>
  <nav class="nav abs"><a>RESIDENTIAL</a><a>COMMERCIAL</a><a>OFF-GRID</a></nav>
  <a class="btn-call abs"><svg width="12" height="12" viewBox="0 0 24 24"><path fill="#fff" d="M6.6 10.8a15 15 0 0 0 6.6 6.6l2.2-2.2c.3-.3.7-.4 1-.2 1.1.4 2.3.6 3.6.6.6 0 1 .4 1 1V20c0 .6-.4 1-1 1A17 17 0 0 1 3 4c0-.6.4-1 1-1h3.5c.6 0 1 .4 1 1 0 1.3.2 2.5.6 3.6.1.3 0 .7-.2 1z"/></svg>CALL US AT: (07) 3550 4182</a>
  <a class="btn-quote abs">FREE QUOTE</a>
</header>

<section class="hero abs">
  <svg class="abs" style="top:0;left:0" width="1200" height="580" viewBox="0 0 1200 580">
    <defs><linearGradient id="heroBg" x1="0" y1="0" x2="0" y2="1"><stop offset="0" stop-color="#c3c6cc"/><stop offset=".6" stop-color="#e4e6ea"/><stop offset="1" stop-color="#f3f4f6"/></linearGradient></defs>
    <path d="M0 0H1200V400L600 580L0 400Z" fill="url(#heroBg)"/>
    <path d="M0 430Q300 340 600 470T1200 420V470L600 580L0 470Z" fill="#fff" opacity=".6"/>
  </svg>
  <div class="abs" role="img" aria-label="Solar panels with pump, controller and hose kit" style="top:140px;left:440px;width:250px;height:450px;background:linear-gradient(160deg,#3a4fa0,#20307a 60%,#c9ccd6);border-radius:4px"></div>
  <div class="save abs" style="top:10px"><span>S</span><span style="margin-top:18px">A</span><span style="margin-top:8px">V</span><span style="margin-top:20px">E</span></div>
</section>
<h1 class="hero-title abs">SUMMER SPECIAL PACKAGE</h1>
<div class="hero-sub abs">6.6KW Tin Roof Special</div>
<div class="old-price abs">$3,299</div>
<div class="new-price abs">$2,877</div>
<a class="btn-dark abs" style="top:375px;left:88px;width:130px;height:47px">GET A QUOTE</a>
<div class="power-title abs">YOUR <b>POWER</b> BILL</div>
<div class="abs" style="top:267px;left:735px;display:grid;grid-template-columns:190px 190px;row-gap:18px">
  <div class="feat"><i></i>6.6kw Power Plant</div><div class="feat"><i></i>25 Year Panel Warranty</div>
  <div class="feat"><i></i>Premium 300 Panel</div><div class="feat"><i></i>10 Year Workmanship</div>
  <div class="feat"><i></i>2019 Model Inverter</div><div class="feat"><i></i>10 Year Inverter Warranty</div>
  <div class="feat"><i></i>WIFI Monitoring System</div>
</div>

<article class="svc abs" style="left:88px">
  <div class="ph" role="img" aria-label="City skyline behind rooftop solar panels" style="background:linear-gradient(#8a96a8,#3f4a5e)"></div>
  <h3>Reduce costs, grow<br>your business</h3>
  <p>If you're running a business, then our Commercial Energy Solutions are...</p>
  <a class="more"><i><svg width="10" height="10" viewBox="0 0 10 10"><path d="M1 5h7M5 2l3 3-3 3" stroke="#fff" fill="none" stroke-width="1.5"/></svg></i>LEARN MORE</a>
</article>
<article class="svc abs" style="left:350px">
  <div class="ph" role="img" aria-label="Solar field at sunset" style="background:linear-gradient(#e2a24a,#6e5a3a)"></div>
  <h3>Avoid blackouts, go<br>off-grid</h3>
  <p>In a country where blackouts &amp; power outages are so common, our Off-Grid Power...</p>
  <a class="more"><i><svg width="10" height="10" viewBox="0 0 10 10"><path d="M1 5h7M5 2l3 3-3 3" stroke="#fff" fill="none" stroke-width="1.5"/></svg></i>LEARN MORE</a>
</article>
<article class="svc abs" style="left:610px">
  <div class="ph" role="img" aria-label="Solar panel irrigating a green field" style="background:linear-gradient(#9cc6e8,#4a8a3a)"></div>
  <h3>Go solar, eliminate<br>fuel cost</h3>
  <p>We know you want to grow so we help you find more cost-efficient alternatives...</p>
  <a class="more"><i><svg width="10" height="10" viewBox="0 0 10 10"><path d="M1 5h7M5 2l3 3-3 3" stroke="#fff" fill="none" stroke-width="1.5"/></svg></i>LEARN MORE</a>
</article>
<article class="svc abs" style="left:872px">
  <div class="ph" role="img" aria-label="Solar panels on a tiled family roof" style="background:linear-gradient(#5a8ad0,#c0582e)"></div>
  <h3>Save money for your<br>family</h3>
  <p>Our Residential Solar Power solutions can give you up to 80% reduction on your...</p>
  <a class="more"><i><svg width="10" height="10" viewBox="0 0 10 10"><path d="M1 5h7M5 2l3 3-3 3" stroke="#fff" fill="none" stroke-width="1.5"/></svg></i>LEARN MORE</a>
</article>

<h2 class="headline abs">FIELDLINE CUT <b>80% OFF</b> THEIR POWER BILL</h2>
<p class="lede abs">Whether you're a huge commercial establishment or a small property owner, Torva Power has the perfect solution to give you consistent savings on your monthly bills.</p>

<section class="quote-box abs">
  <h2>FREE NO OBLIGATION QUOTE!</h2>
  <div class="q-sub">Get a FREE customized Quote For your Home or Business!</div>
  <div class="field" style="top:150px;left:56px;width:227px;height:44px">Name*</div>
  <div class="field" style="top:150px;left:290px;width:226px;height:44px">Email address*</div>
  <div class="field" style="top:204px;left:56px;width:227px;height:44px">Phone number*</div>
  <div class="field" style="top:204px;left:290px;width:226px;height:44px">Postcode*</div>
  <div class="field" style="top:258px;left:56px;width:460px;height:44px">Commercial*</div>
  <div class="field tall" style="top:312px;left:56px;width:460px;height:164px">Message*</div>
  <div class="btn-white">GET FREE QUOTE</div>
  <svg class="abs" style="left:0;top:596px" width="737" height="60" viewBox="0 0 737 60"><path d="M0 40Q120 0 250 35T500 30T737 25V60H0Z" fill="#d13038"/></svg>
</section>
<div class="abs" role="img" aria-label="Installer in hard hat fitting a solar panel" style="top:1454px;left:662px;width:450px;height:439px;background:linear-gradient(150deg,#3a86d8,#2c4f96 60%,#3a3f4c);box-shadow:0 16px 40px rgba(0,0,0,.25)"></div>

<h2 class="sec-title abs" style="top:2080px">Our Products</h2>
<div class="prod abs" style="left:88px"><div class="box"><div role="img" aria-label="Pair of solar panels" style="width:140px;height:200px;background:linear-gradient(135deg,#2c3f96,#1a265e)"></div></div><h4>PRODUCT HEADING</h4><div class="price">$25.00</div><a class="btn-red">LEARN MORE</a></div>
<div class="prod abs" style="left:351px"><div class="box"><div role="img" aria-label="Solar panel with submersible pumps" style="width:170px;height:220px;background:linear-gradient(#3a5ab0,#b8bcc6)"></div></div><h4>PRODUCT HEADING</h4><div class="price">$25.00</div><a class="btn-red">LEARN MORE</a></div>
<div class="prod abs" style="left:613px"><div class="box"><div role="img" aria-label="Solar panel above a surface pump" style="width:180px;height:220px;background:linear-gradient(#3a5ab0,#2a2c32)"></div></div><h4>PRODUCT HEADING</h4><div class="price">$25.00</div><a class="btn-red">LEARN MORE</a></div>
<div class="prod abs" style="left:876px"><div class="box"><div role="img" aria-label="Solar pump kit with controller" style="width:150px;height:220px;background:linear-gradient(#2c3f96,#c6cad2)"></div></div><h4>PRODUCT HEADING</h4><div class="price">$25.00</div><a class="btn-red">LEARN MORE</a></div>

<div class="rule abs" style="top:2662px"></div>

<h2 class="sec-title abs" style="top:2742px">Go Solar &amp; Grow Your Business</h2>
<div class="abs" role="img" aria-label="Worker in hard hat carrying a solar panel" style="top:2800px;left:88px;width:492px;height:290px;background:linear-gradient(140deg,#9aa0a8,#4a6a9a)"></div>
<div class="abs" role="img" aria-label="Rows of solar panels at sunset" style="top:2800px;left:620px;width:492px;height:290px;background:linear-gradient(#e0a860,#5a5e6e)"></div>
<article class="grow-card abs" style="left:106px"><h3>A more cost-efficient alternative to<br>your irrigation needs</h3><p>Conventional water pump systems can be quite costly. Volatile prices of fuel and other related expenses contribute to adding massive burden to your operations. Torva Power offers you a more cost-efficient alternative through...</p></article>
<article class="grow-card abs" style="left:636px"><h3>A more cost-efficient alternative to<br>your irrigation needs</h3><p>Torva Power has a full range of energy management solutions that will help your business reduce energy costs. In addition, we will also help you in maximising your available tax deductions while shortening your payback period...</p></article>

<h2 class="sec-title abs" style="top:3302px">Why do you need to go solar?</h2>
<div class="why abs" style="left:70px"><div class="icon"><svg width="54" height="54" viewBox="0 0 54 54" fill="none" stroke="#fff" stroke-width="3"><ellipse cx="22" cy="12" rx="14" ry="5"/><path d="M8 12v24c0 3 6 5 14 5M36 12v8"/><path d="M8 24c0 3 6 5 14 5"/><circle cx="38" cy="38" r="11"/><path d="M38 32v6l4 3"/></svg></div><p>Get consistent<br>savings for 20+ years</p></div>
<div class="why abs" style="left:290px"><div class="icon"><svg width="54" height="54" viewBox="0 0 54 54" fill="none" stroke="#fff" stroke-width="3"><circle cx="27" cy="14" r="7"/><path d="M27 2v3M27 23v3M15 14h-3M42 14h-3M18 5l2 2M36 5l-2 2"/><path d="M12 30l10 8v12M42 30l-10 8v12"/></svg></div><p>Be independent from<br>the grid</p></div>
<div class="why abs" style="left:505px"><div class="icon dark"><svg width="54" height="54" viewBox="0 0 54 54" fill="#fff"><rect x="8" y="34" width="7" height="14"/><rect x="19" y="28" width="7" height="20"/><rect x="30" y="22" width="7" height="26"/><rect x="41" y="16" width="7" height="32"/><path d="M6 28L20 16l8 6L44 6" stroke="#fff" stroke-width="3" fill="none"/></svg></div><p>Increase and maximise<br>your bottomline</p></div>
<div class="why abs" style="left:728px"><div class="icon"><svg width="54" height="54" viewBox="0 0 54 54" fill="none" stroke="#fff" stroke-width="3"><circle cx="25" cy="29" r="20"/><circle cx="25" cy="29" r="12"/><circle cx="25" cy="29" r="4" fill="#fff"/><path d="M25 29L46 8M40 8h6v6"/></svg></div><p>Differentiate your business<br>against competitors</p></div>
<div class="why abs" style="left:947px"><div class="icon"><svg width="54" height="54" viewBox="0 0 54 54" fill="none" stroke="#fff" stroke-width="3"><circle cx="24" cy="32" r="17"/><path d="M12 26c6 2 8 8 14 6s4 10 10 8"/><path d="M42 6v18M42 24a4 4 0 1 0 .1 0"/></svg></div><p>Take part in solving<br>global warming</p></div>

<div class="abs" role="img" aria-label="Hands holding a tablet showing business charts" style="top:3580px;left:88px;width:487px;height:390px;background:linear-gradient(135deg,#7c8696,#e6e8ec 55%,#5a4a44);box-shadow:0 16px 40px rgba(0,0,0,.2)"></div>
<div class="feature-text abs"><h2>Increase and maximise your bottomline</h2><p>Saving money on electricity costs is only half of the equation. The money you save can be used on other revenue-generating activities. Combining this will result in maximising your profits and increasing your bottomline. Giving you more 'power' to reach new heights for your business!</p></div>

<h2 class="sec-title abs" style="top:4054px">Here's what our clients are saying</h2>
<div class="abs" style="top:4130px;left:412px;width:376px;height:90px">
  <div class="avatar abs" role="img" aria-label="Client portrait" style="left:5px;top:18px;width:46px;height:46px;background:#d8c8b8"></div>
  <div class="avatar abs" role="img" aria-label="Client portrait" style="left:80px;top:18px;width:46px;height:46px;background:#c8ccd4"></div>
  <div class="avatar abs" role="img" aria-label="Featured client portrait" style="left:144px;top:0;width:88px;height:88px;background:#b89a80;border:4px solid #fff;box-shadow:0 4px 14px rgba(0,0,0,.2)"></div>
  <div class="avatar abs" role="img" aria-label="Client portrait" style="left:252px;top:18px;width:46px;height:46px;background:#c4c8cf"></div>
  <div class="avatar abs" role="img" aria-label="Client portrait" style="left:326px;top:18px;width:46px;height:46px;background:#c9a888"></div>
</div>
<div class="qmark abs" style="top:4220px;left:254px">“</div>
<div class="qmark abs" style="top:4295px;left:694px">”</div>
<div class="testi abs">
  <div class="stars">★★★★★</div>
  <q>Have been a pleasure to deal with and came up with a combinations of ideas to save money</q>
  <div class="name">DELPHINE</div>
  <div class="role">Client</div>
</div>
<svg class="abs" style="top:4215px;left:1100px" width="16" height="50" viewBox="0 0 16 50"><circle cx="8" cy="8" r="5" fill="none" stroke="#2d3340" stroke-width="2.5"/><circle cx="8" cy="27" r="3" fill="none" stroke="#b9bcc4"/><circle cx="8" cy="42" r="3" fill="none" stroke="#b9bcc4"/></svg>

<div class="rule abs" style="top:4455px"></div>
<div class="abs" style="top:4488px;left:88px;width:1024px;display:flex;justify-content:space-around;align-items:center">
  <span role="img" aria-label="Partner badge" style="width:130px;height:30px;background:#e3e5e9;border-radius:4px"></span>
  <span role="img" aria-label="Partner badge" style="width:90px;height:46px;background:#e3e5e9;border-radius:50%"></span>
  <span role="img" aria-label="Partner badge" style="width:140px;height:30px;background:#e3e5e9;border-radius:4px"></span>
  <span role="img" aria-label="Partner badge" style="width:140px;height:36px;background:#e3e5e9;border-radius:4px"></span>
  <span role="img" aria-label="Partner badge" style="width:74px;height:46px;background:#e3e5e9"></span>
</div>

<footer class="footer abs">
  <div class="brand abs" style="top:148px;left:88px">
    <span class="brand-mark"></span>
    <div><div class="brand-name" style="font-size:26px">Torva Power</div><div class="brand-tag" style="color:#cfd2d8">ENGINEERING AND ECONOMIC SOLUTIONS</div></div>
  </div>
  <div class="f-col abs" style="top:82px;left:395px"><h5>Quick Links</h5><ul><li>Home</li><li>Residential</li><li>Commercial</li><li>Off-Grid</li><li>Contact Us</li></ul></div>
  <div class="f-col abs" style="top:82px;left:598px"><h5>Information</h5><ul><li>Terms &amp; Condition</li><li>Privacy Policy</li><li>Faq</li><li>Customer Service</li><li>FAQ</li></ul></div>
  <div class="f-col abs" style="top:82px;left:810px;width:300px"><h5>Contact Us</h5>
    <div class="contact-item"><svg width="14" height="14" viewBox="0 0 24 24"><path fill="#c8222b" d="M6.6 10.8a15 15 0 0 0 6.6 6.6l2.2-2.2c.3-.3.7-.4 1-.2 1.1.4 2.3.6 3.6.6.6 0 1 .4 1 1V20c0 .6-.4 1-1 1A17 17 0 0 1 3 4c0-.6.4-1 1-1h3.5c.6 0 1 .4 1 1 0 1.3.2 2.5.6 3.6.1.3 0 .7-.2 1z"/></svg><div><b>Phone</b><span>(07) 3550 4182</span></div></div>
    <div class="contact-item"><svg width="14" height="14" viewBox="0 0 24 24"><path fill="#c8222b" d="M12 2a7 7 0 0 0-7 7c0 5 7 13 7 13s7-8 7-13a7 7 0 0 0-7-7zm0 9.5A2.5 2.5 0 1 1 12 6.5a2.5 2.5 0 0 1 0 5z"/></svg><div><b>Address</b><span>48-52 Harlow Street Kenmore QLD 4069</span></div></div>
    <div class="contact-item"><svg width="14" height="14" viewBox="0 0 24 24"><circle cx="12" cy="12" r="10" fill="#c8222b"/><path d="M12 6v6l4 2" stroke="#fff" stroke-width="2" fill="none"/></svg><div><b>Timing</b><span>Monday - Friday: 9:00AM - 5:00PM</span></div></div>
  </div>
  <div class="abs" style="top:358px;left:88px;width:1024px;height:1px;background:rgba(255,255,255,.12)"></div>
  <div class="copy">Copyright 2019 Torva Power, All Rights Reserved.</div>
  <div class="to-top"><svg width="12" height="12" viewBox="0 0 12 12"><path d="M6 11V2M2 6l4-4 4 4" stroke="#fff" stroke-width="1.6" fill="none"/></svg></div>
</footer>

</body>
</html>
```